Harborlight Church Next Steps- These are basic steps people for to continue their spiritual journey

The goal of this graphic is to explain the next steps for a person on their spiritual journey. Here are the following steps we would like included in the graphic: Believe, Baptism, Worship, Serve, Community Groups, Give, Bible Reading & Prayer, Share the Gospel, Outreach, and Learn with Believe being the centrally featured step. There is no specific order to the steps but again we would like Believe centrally featured. Our leadership team has thought about the idea of a tree or a wheel as the theme, but we are not tied to that. In fact, we would love for creative designers to present their own ideas on the theme. I am attaching our logo to give you an idea of our previous designs. You can coordinate designs if you would like, but it is not necessary. Thanks for your work on this!
Target Market(s)
Harborlight Church Team Members
Industry/Entity Type
Church
Colors
Designer to choose colors to be used in the design.
Requirements
Must have
- Include all the steps with the title Harborlight Next Steps (This title could be adjusted depending on the theme)
Nice to have
- Variety of colors
Should not have
- No traditional church artwork whatsoever. We want this to be progressive in design.

```html
<!DOCTYPE html>
<html lang="en">
<head>
<meta charset="utf-8">
<title>Harborlight Next Steps</title>
<link rel="stylesheet" href="https://fonts.googleapis.com/css2?family=Lilita+One&display=swap">
<style>
  :root {
    --title-blue: #4d93d2;
    --logo-blue: #5b9bd5;
    --ink: #262626;
    --baptism-ink: #2f3a8f;
    --believe-red: #c11f2f;
    --orange-light: #f7925a;
    --orange-dark: #f0662a;
    --green: #7cc04a;
    --teal: #1fab98;
    --blue: #2357a8;
    --indigo: #433c86;
    --magenta: #8e2a8a;
    --violet: #5b2d8e;
    --purple-ink: #6a2a92;
    --hub-light: #ffffff;
    --hub-grey: #dfe2e8;
  }
  html, body {
    margin: 0;
    padding: 0;
    width: 1028px;
    height: 1200px;
    overflow: hidden;
    background: #ffffff;
  }
  .next-steps {
    display: block;
    width: 1028px;
    height: 1200px;
    font-family: "Lilita One", sans-serif;
  }
  .brand-name { fill: var(--ink); font-size: 38px; }
  .brand-mark { fill: var(--logo-blue); }
  .title { fill: var(--title-blue); font-size: 150px; letter-spacing: -2px; }
  .title-shadow { fill: #d9dde3; font-size: 150px; letter-spacing: -2px; }
  .label-white { fill: #ffffff; }
  .label-baptism { fill: var(--baptism-ink); font-size: 64px; }
  .label-believe { fill: var(--believe-red); font-size: 80px; }
  .label-community { fill: var(--orange-dark); }
  .label-serve { fill: var(--teal); }
  .label-prayer { fill: var(--purple-ink); }
  .icon-slot { fill: #ffffff; fill-opacity: 0.22; }
  .connector { stroke-width: 9; stroke-dasharray: 14 14; fill: none; }
</style>
</head>
<body>
<svg class="next-steps" viewBox="0 0 1190 1390" preserveAspectRatio="none" xmlns="http://www.w3.org/2000/svg">
  <defs>
    <linearGradient id="grad-green" x1="0" y1="0" x2="1" y2="0">
      <stop offset="0" stop-color="var(--green)"/><stop offset="1" stop-color="var(--teal)"/>
    </linearGradient>
    <linearGradient id="grad-orange" x1="0" y1="0" x2="1" y2="0">
      <stop offset="0" stop-color="var(--orange-light)"/><stop offset="1" stop-color="var(--orange-dark)"/>
    </linearGradient>
    <linearGradient id="grad-blue" x1="0" y1="0" x2="1" y2="0">
      <stop offset="0" stop-color="var(--blue)"/><stop offset="1" stop-color="var(--indigo)"/>
    </linearGradient>
    <linearGradient id="grad-purple" x1="0" y1="0" x2="1" y2="0">
      <stop offset="0" stop-color="var(--magenta)"/><stop offset="1" stop-color="var(--violet)"/>
    </linearGradient>
    <radialGradient id="grad-hub" cx="0.4" cy="0.35" r="0.75">
      <stop offset="0" stop-color="var(--hub-light)"/><stop offset="1" stop-color="var(--hub-grey)"/>
    </radialGradient>
    <filter id="hub-shadow" x="-30%" y="-30%" width="160%" height="160%">
      <feDropShadow dx="0" dy="6" stdDeviation="10" flood-color="#000" flood-opacity="0.18"/>
    </filter>
  </defs>

  <!-- Brand -->
  <g class="brand">
    <circle class="brand-mark" cx="472" cy="82" r="34"/>
    <text class="brand-name" x="520" y="96">Harborlight Church</text>
  </g>

  <!-- Title -->
  <text class="title-shadow" x="588" y="268" text-anchor="middle">Next Steps</text>
  <text class="title" x="582" y="262" text-anchor="middle">Next Steps</text>

  <!-- Connectors -->
  <g class="connectors">
    <line class="connector" stroke="#1a8f4a" x1="469" y1="715" x2="375" y2="621"/>
    <line class="connector" stroke="var(--baptism-ink)" x1="582" y1="668" x2="582" y2="618"/>
    <line class="connector" stroke="var(--orange-dark)" x1="695" y1="715" x2="789" y2="621"/>
    <line class="connector" stroke="var(--orange-dark)" x1="422" y1="828" x2="372" y2="828"/>
    <line class="connector" stroke="#1a8f4a" x1="742" y1="828" x2="792" y2="828"/>
    <line class="connector" stroke="var(--baptism-ink)" x1="469" y1="941" x2="375" y2="1035"/>
    <line class="connector" stroke="var(--purple-ink)" x1="582" y1="988" x2="582" y2="1038"/>
    <line class="connector" stroke="var(--purple-ink)" x1="695" y1="941" x2="789" y2="1035"/>
  </g>

  <!-- Give -->
  <g class="step step-give">
    <path fill="url(#grad-green)" d="M75,602.3 A555,555 0 0 1 347.5,325 L460.7,567.9 A287,287 0 0 0 319.8,711.3 Z"/>
    <rect class="icon-slot" x="205" y="445" width="170" height="120" rx="20" role="img" aria-label="Icon of open hands holding a heart"/>
    <text class="label-white" x="272" y="612" text-anchor="middle" font-size="58">Give</text>
  </g>

  <!-- Baptism -->
  <g class="step step-baptism">
    <text class="label-baptism" x="592" y="415" text-anchor="middle">Baptism</text>
    <path fill="url(#grad-blue)" d="M446.9,456.8 A395,395 0 0 1 717.1,456.8 L655.5,626 A215,215 0 0 0 508.5,626 Z"/>
    <rect class="icon-slot" x="512" y="476" width="130" height="84" rx="16" role="img" aria-label="Icon of water"/>
  </g>

  <!-- Worship -->
  <g class="step step-worship">
    <path fill="url(#grad-orange)" d="M816.5,325 A555,555 0 0 1 1089,602.3 L844.2,711.3 A287,287 0 0 0 703.3,567.9 Z"/>
    <rect class="icon-slot" x="815" y="420" width="140" height="135" rx="20" role="img" aria-label="Icon of a person in prayer"/>
    <text class="label-white" x="893" y="600" text-anchor="middle" font-size="56">Worship</text>
  </g>

  <!-- Community Groups -->
  <g class="step step-community">
    <path fill="url(#grad-orange)" d="M210.8,963.1 A395,395 0 0 1 210.8,692.9 L380,754.5 A215,215 0 0 0 380,901.5 Z"/>
    <rect class="icon-slot" x="228" y="772" width="112" height="112" rx="18" role="img" aria-label="Icon of a small group gathered together"/>
    <text class="label-community" transform="translate(126,832) rotate(-90)" text-anchor="middle" font-size="56">Community</text>
    <text class="label-community" transform="translate(167,832) rotate(-90)" text-anchor="middle" font-size="48">Groups</text>
  </g>

  <!-- Serve and Outreach -->
  <g class="step step-serve">
    <path fill="url(#grad-green)" d="M953.2,692.9 A395,395 0 0 1 953.2,963.1 L784,901.5 A215,215 0 0 0 784,754.5 Z"/>
    <rect class="icon-slot" x="825" y="760" width="105" height="120" rx="18" role="img" aria-label="Icon of a person with open arms"/>
    <text class="label-serve" transform="translate(1058,832) rotate(90)" text-anchor="middle" font-size="56">Serve</text>
    <text class="label-serve" transform="translate(1027,832) rotate(90)" text-anchor="middle" font-size="28">and</text>
    <text class="label-serve" transform="translate(994,832) rotate(90)" text-anchor="middle" font-size="50">Outreach</text>
  </g>

  <!-- Learn -->
  <g class="step step-learn">
    <path fill="url(#grad-blue)" d="M347.5,1331 A555,555 0 0 1 75,1053.7 L319.8,944.7 A287,287 0 0 0 460.7,1088.1 Z"/>
    <rect class="icon-slot" x="200" y="1092" width="165" height="34" rx="10" role="img" aria-label="Icon of an open book"/>
    <text class="label-white" x="282" y="1182" text-anchor="middle" font-size="66">Learn</text>
  </g>

  <!-- Bible Reading and Prayer -->
  <g class="step step-prayer">
    <path fill="url(#grad-purple)" d="M717.1,1199.2 A395,395 0 0 1 446.9,1199.2 L508.5,1030 A215,215 0 0 0 655.5,1030 Z"/>
    <rect class="icon-slot" x="505" y="1095" width="155" height="80" rx="16" role="img" aria-label="Icons of a person reading the Bible and praying hands"/>
    <text class="label-prayer" x="582" y="1254" text-anchor="middle" font-size="32">Bible Reading</text>
    <text class="label-prayer" x="582" y="1285" text-anchor="middle" font-size="32">and</text>
    <text class="label-prayer" x="582" y="1335" text-anchor="middle" font-size="60">Prayer</text>
  </g>

  <!-- Share the Gospel -->
  <g class="step step-gospel">
    <path fill="url(#grad-purple)" d="M1089,1053.7 A555,555 0 0 1 816.5,1331 L703.3,1088.1 A287,287 0 0 0 844.2,944.7 Z"/>
    <rect class="icon-slot" x="818" y="1010" width="122" height="110" rx="18" role="img" aria-label="Icon of one person sharing with a growing network of people"/>
    <text class="label-white" x="880" y="1150" text-anchor="middle" font-size="30">Share the</text>
    <text class="label-white" x="868" y="1206" text-anchor="middle" font-size="64">Gospel</text>
  </g>

  <!-- Believe hub -->
  <g class="hub">
    <circle cx="582" cy="828" r="150" fill="url(#grad-hub)" filter="url(#hub-shadow)"/>
    <rect x="510" y="730" width="130" height="105" rx="14" fill="var(--believe-red)" fill-opacity="0.16" role="img" aria-label="Graphic of three crosses on a hill"/>
    <text class="label-believe" x="582" y="900" text-anchor="middle">Believe</text>
  </g>
</svg>
</body>
</html>
```